HWN Structures Ltd- building and maintenance company looking to create professional branding for m

creation of a website for a building and maintenance company,
will need a gallery and references/ reviews page
homepage to have some company information with rolling photos of completed works
all suggestions welcome on additional requirements for website.
layout should be easy to navigate.

Target Market(s)

30-70s homeowners with mid to high income

Logo Text

HWN Structures Ltd

Coding

Coded - Design and coding required

Number of Pages Required

4 page

```html
<!DOCTYPE html>
<html lang="en">
<head>
<meta charset="utf-8">
<title>HWN Structures Ltd – Building and Maintenance</title>
<link href="https://fonts.googleapis.com/css2?family=Poppins:wght@400;500;600;700;800&display=swap" rel="stylesheet">
<style>
:root{
  --amber:#fbaa00;
  --ink:#111111;
  --black:#000000;
  --white:#ffffff;
  --grey-band:#6c6c6c;
  --text:#333333;
  --muted:#777777;
  --canvas:#ececec;
}
*{margin:0;padding:0;box-sizing:border-box}
html,body{width:1200px;height:3158px;overflow:hidden}
body{background:var(--canvas);font-family:'Poppins',sans-serif;color:var(--text)}
.page{position:absolute;left:200px;top:134px;width:800px;height:2889px;background:var(--white);overflow:hidden;box-shadow:0 10px 40px rgba(0,0,0,.25)}
.abs{position:absolute}
.accent{color:var(--amber)}
.btn{position:absolute;background:var(--amber);color:var(--white);font-weight:600;text-transform:uppercase;display:flex;align-items:center;justify-content:center;letter-spacing:.3px}

/* top bar + nav */
.topbar{left:0;top:0;width:800px;height:15px;background:var(--amber);font-size:6px;color:var(--ink)}
.topbar span{position:absolute;top:3px;display:flex;align-items:center;gap:3px}
.nav{left:0;top:15px;width:800px;height:41px;background:var(--black);color:var(--white)}
.brand{position:absolute;left:64px;top:13px;font-size:12px;font-weight:600;letter-spacing:.2px}
.brand b{display:inline-block;width:1px;height:14px;background:var(--white);vertical-align:middle;margin:0 4px}
.menu{position:absolute;right:72px;top:17px;display:flex;gap:26px;font-size:7px;font-weight:500}

/* hero */
.hero{left:0;top:56px;width:800px;height:397px}
.hero-bg{position:absolute;inset:0;background:linear-gradient(90deg,#2a2620 0%,#3b3327 45%,#5a4a36 70%,#4a3e30 100%)}
.hero-photo{position:absolute;left:453px;top:0;width:347px;height:397px;background:radial-gradient(ellipse at 45% 45%,#6e5a44 0%,#3a3128 70%)}
.hero-cut{position:absolute;left:0;top:0}
.hero-kicker{left:64px;top:84px;font-size:18px;font-weight:600;color:var(--white)}
.hero-title{left:62px;top:100px;font-size:54px;font-weight:800;color:var(--white);letter-spacing:1px;line-height:1.2}
.hero-lead{left:64px;top:157px;width:290px;font-size:10.5px;line-height:1.45;color:#e8e8e8}

/* section titles */
.sec-title{position:absolute;left:0;width:800px;text-align:center;font-size:21px;font-weight:700;color:var(--ink)}
.sec-title::after{content:"";display:block;width:80px;height:1px;background:var(--amber);margin:1px auto 0;opacity:.6}
.view-link{position:absolute;font-size:8px;font-weight:500;color:var(--ink)}

/* services */
.card{position:absolute;top:586px;width:148px;height:199px;background:var(--white);box-shadow:0 2px 8px rgba(0,0,0,.18);text-align:center}
.card .pic{position:absolute;left:37px;top:12px;width:73px;height:73px;border-radius:50%}
.card h3{position:absolute;top:98px;width:100%;font-size:12px;font-weight:500;color:var(--amber)}
.card p{position:absolute;top:119px;left:12px;width:124px;font-size:7.5px;line-height:1.4;color:#555}
.card .btn{left:46px;top:169px;width:56px;height:13px;font-size:6px}
.arrow{position:absolute;top:675px}

/* cost band */
.cost{left:0;top:828px;width:800px;height:245px;background:var(--grey-band)}
.cost-photo{position:absolute;left:331px;top:0;width:469px;height:245px;background:linear-gradient(90deg,#6c6c6c 0%,#5d5650 35%,#7a6a5c 60%,#8a6a4a 85%,#6c6c6c 100%)}
.cost h2{position:absolute;left:56px;top:44px;font-size:21px;font-weight:500;line-height:1.25;color:var(--white)}
.cost p{position:absolute;left:56px;top:110px;width:270px;font-size:10.5px;line-height:1.42;color:#e6e6e6}

/* about */
.about-photo{left:49px;top:1130px;width:339px;height:206px;background:linear-gradient(135deg,#3f4650 0%,#5b6470 45%,#2c3138 100%)}
.about h2{position:absolute;left:449px;top:1122px;font-size:27px;font-weight:700;line-height:1.45;color:var(--ink)}
.about p{position:absolute;left:449px;top:1204px;width:310px;font-size:10.5px;line-height:1.45;color:#333}

/* gallery */
.shot{position:absolute}

/* team */
.team-lead{left:0;top:1798px;width:800px;text-align:center;font-size:10.5px;line-height:1.45;color:#333}
.member{position:absolute;top:1851px;width:240px;text-align:center}
.member .face{width:88px;height:88px;border-radius:50%;margin:0 auto;background:radial-gradient(circle at 50% 45%,#e9eef3 0%,#cdd7e1 100%)}
.member h4{margin-top:18px;font-size:11px;font-weight:500;color:var(--amber);letter-spacing:.5px}
.member .role{font-size:6px;color:#555;text-transform:uppercase}
.member .tel{margin-top:6px;font-size:11px;color:var(--amber)}
.member .mail{margin-top:5px;font-size:6.5px;color:#555}

/* work band */
.work{left:0;top:2098px;width:800px;height:244px;background:linear-gradient(90deg,#4b4f57 0%,#6d7078 50%,#55585f 100%)}
.work h2{position:absolute;left:0;top:40px;width:800px;text-align:center;font-size:21px;font-weight:700;color:var(--white)}
.work p{position:absolute;left:125px;top:100px;width:560px;font-size:10.5px;line-height:1.42;color:#eeeeee}

/* feedback */
.say-box{left:34px;top:2437px;width:392px;height:115px;background:var(--amber)}
.say-box h3{position:absolute;left:76px;top:32px;font-size:22px;font-weight:700;line-height:1.55;color:var(--white)}
.quote-card{left:331px;top:2474px;width:427px;height:163px;background:var(--white);box-shadow:0 2px 10px rgba(0,0,0,.15)}
.quote-card .avatar{position:absolute;left:185px;top:-29px;width:58px;height:58px;border-radius:50%;background:radial-gradient(circle,#f1ede8 0%,#d9d2ca 100%);border:2px solid var(--white)}
.quote-card p{position:absolute;left:20px;top:72px;width:390px;text-align:center;font-size:8px;line-height:1.45;color:#333}
.quote-card .qmark{position:absolute;font-size:14px;font-weight:700;color:var(--amber)}
.quote-card .who{position:absolute;right:48px;top:117px;font-size:8px;font-weight:600;color:var(--ink)}
.round{position:absolute;top:2583px;width:27px;height:27px;border-radius:50%;background:var(--amber)}

/* footer */
.footer{left:0;top:2686px;width:800px;height:203px}
.footer .col{position:absolute;top:93px;color:var(--white);font-size:7.5px;line-height:1.45}
.footer .col h5{font-size:7.5px;font-weight:500;margin-bottom:8px;color:var(--white)}
.footer .links{color:#cccccc}
.f-brand{position:absolute;left:75px;top:85px;font-size:15px;font-weight:600;color:var(--white)}
.f-blurb{position:absolute;left:75px;top:111px;width:170px;font-size:6px;line-height:1.4;color:#cccccc}
.copy{position:absolute;left:0;top:187px;width:800px;text-align:center;font-size:7px;color:#cccccc}
.dot{display:inline-block;width:7px;height:7px;border-radius:50%;background:var(--white);margin-right:4px}
</style>
</head>
<body>
<main class="page">

  <!-- top bar -->
  <div class="abs topbar">
    <span style="left:440px">
      <svg width="7" height="7" viewBox="0 0 10 10"><path d="M2 1l2 2-1 1.5c.6 1.3 1.5 2.2 2.5 2.5L7 6l2 2-1.2 1.2C4.5 9 1 5.5.8 2.2z" fill="#111"/></svg>
      +1 (555) 0142 738</span>
    <span style="left:557px">
      <svg width="8" height="6" viewBox="0 0 10 7"><rect x=".5" y=".5" width="9" height="6" fill="none" stroke="#111"/><path d="M.5 .5l4.5 3.5 4.5-3.5" fill="none" stroke="#111"/></svg>
      hello@hwnstructures.example</span>
  </div>

  <!-- navigation -->
  <header class="abs nav">
    <div class="brand">HWN<b></b>STRUCTURES LTD</div>
    <nav class="menu"><span>HOME</span><span>SERVICE</span><span>PROJECTS</span><span>ABOUT US</span><span>CONTACT US</span></nav>
  </header>

  <!-- hero -->
  <section class="abs hero">
    <div class="hero-bg"></div>
    <div class="hero-photo" role="img" aria-label="Woman construction worker in a yellow hard hat and safety glasses on a building site"></div>
    <svg class="hero-cut" width="800" height="397" viewBox="0 0 800 397"><polygon points="0,306 400,397 800,306 800,397 0,397" fill="#ffffff"/></svg>
    <div class="abs hero-kicker">BUILDING <span class="accent">AND</span> MAINTENANCE</div>
    <h1 class="abs hero-title">COMPNAY</h1>
    <p class="abs hero-lead">whether you require a one off service or require multiple service contracts, we can provide the solution for you.</p>
    <div class="btn" style="left:64px;top:199px;width:98px;height:20px;font-size:8px">Contact us</div>
  </section>

  <!-- services -->
  <h2 class="sec-title" style="top:519px">SERVICES <span class="accent">WE OFFER</span></h2>
  <div class="view-link" style="left:660px;top:551px">View More &nbsp;&nbsp;&nbsp;›</div>

  <svg class="arrow" style="left:45px" width="10" height="16" viewBox="0 0 10 16"><path d="M8 2L2 8l6 6" fill="none" stroke="#111" stroke-width="1.6"/></svg>
  <svg class="arrow" style="left:750px" width="10" height="16" viewBox="0 0 10 16"><path d="M2 2l6 6-6 6" fill="none" stroke="#111" stroke-width="1.6"/></svg>

  <article class="card" style="left:79px">
    <div class="pic" role="img" aria-label="Electrical panel with breakers" style="background:radial-gradient(circle,#c9cdd2 0%,#7c838b 100%)"></div>
    <h3>ELECTRICAL</h3>
    <p>we are specialists in all aspects of domestic and commercial plumbing, heating and boiler services.</p>
    <div class="btn">Read more</div>
  </article>
  <article class="card" style="left:244px">
    <div class="pic" role="img" aria-label="Plumber fitting a copper pipe" style="background:radial-gradient(circle,#d9b98a 0%,#8a6a44 100%)"></div>
    <h3>PLUMBING</h3>
    <p>we are specialists in all aspects of domestic and commercial plumbing, heating and boiler services.</p>
    <div class="btn">Read more</div>
  </article>
  <article class="card" style="left:411px">
    <div class="pic" role="img" aria-label="Electrical panel with breakers" style="background:radial-gradient(circle,#c9cdd2 0%,#7c838b 100%)"></div>
    <h3>ELECTRICAL</h3>
    <p>we are specialists in all aspects of domestic and commercial plumbing, heating and boiler services.</p>
    <div class="btn">Read more</div>
  </article>
  <article class="card" style="left:576px">
    <div class="pic" role="img" aria-label="Worker laying floor tiles" style="background:radial-gradient(circle,#eeeeee 0%,#9a8f88 100%)"></div>
    <h3>FLOORING</h3>
    <p>we are specialists in all aspects of domestic and commercial plumbing, heating and boiler services.</p>
    <div class="btn">Read more</div>
  </article>

  <!-- cost effective band -->
  <section class="abs cost">
    <div class="cost-photo" role="img" aria-label="Smiling male and female maintenance workers in overalls"></div>
    <h2>Looking for <span class="accent">cost effective</span><br>Maintenance services?</h2>
    <p>we provide reactive building and property maintenance services across the whole of the city. all our tradesmen are fully qualified, very experienced and have years of know how.</p>
    <div class="btn" style="left:56px;top:194px;width:101px;height:20px;font-size:8px">Contact us</div>
  </section>

  <!-- about -->
  <section class="about">
    <div class="abs about-photo" role="img" aria-label="Engineer in hard hat and overalls standing in a factory workshop"></div>
    <h2>ABOUT <span class="accent">HWN</span><br><span class="accent">STRUCTURES</span></h2>
    <p>lorem ipsum dolor sit amet, consectetur adipiscing elit. lorem tellus justo, imperdiet eu id laoreet eu amet, et. cursus faucibus enim et dolor lorem neque. libero orci nec aenean risus, fringilla. purus convallis vitae erat ac aliquam senectus pellentesque sagittis.</p>
    <div class="btn" style="left:449px;top:1314px;width:90px;height:21px;font-size:8px;font-weight:500">Read more</div>
  </section>

  <!-- projects -->
  <h2 class="sec-title" style="top:1391px">TOTAL <span class="accent">PROJECTS</span></h2>
  <div class="view-link" style="left:728px;top:1409px">View All &nbsp;›</div>
  <div class="shot" role="img" aria-label="Worker in protective suit and gloves cleaning a ventilation duct" style="left:24px;top:1443px;width:292px;height:257px;background:linear-gradient(135deg,#d7d7d7 0%,#8d8d8d 50%,#3a3a3a 100%)"></div>
  <div class="shot" role="img" aria-label="Electrician in hard hat working on a switchboard" style="left:322px;top:1443px;width:219px;height:134px;background:linear-gradient(135deg,#8a98a6 0%,#4c5866 100%)"></div>
  <div class="shot" role="img" aria-label="Hand testing a fuse box with a screwdriver" style="left:545px;top:1443px;width:232px;height:134px;background:linear-gradient(135deg,#e6e6e6 0%,#a8a8a8 60%,#c9935a 100%)"></div>
  <div class="shot" role="img" aria-label="Roofer working on a tiled roof under blue sky" style="left:322px;top:1583px;width:219px;height:117px;background:linear-gradient(180deg,#9fc2e0 0%,#6d8fb0 50%,#2e4f6a 100%)"></div>
  <div class="shot" role="img" aria-label="Technician installing a ceiling fixture" style="left:545px;top:1583px;width:232px;height:117px;background:linear-gradient(135deg,#f0f0f0 0%,#b9b9b9 60%,#5b6a8a 100%)"></div>

  <!-- team -->
  <h2 class="sec-title" style="top:1741px">PROFESSIONAL <span class="accent">TEAM</span></h2>
  <p class="abs team-lead">lorem ipsum dolor sit amet, consectetur adipisicing elit, sed do eiusmod<br>tempor incididunt ut labore et dolore magna aliqua. ut enim ad min.</p>
  <div class="member" style="left:17px">
    <div class="face" role="img" aria-label="Portrait of team member in yellow hard hat"></div>
    <h4>MARTIN HALE</h4><div class="role">Lifts maintainers</div>
    <div class="tel">+1 (555) 0142 738</div><div class="mail">MAIL@EXAMPLE.TLD</div>
  </div>
  <div class="member" style="left:260px">
    <div class="face" role="img" aria-label="Portrait of team member in yellow hard hat"></div>
    <h4>DANA COLE</h4><div class="role">Fire alarm maintainers</div>
    <div class="tel">+1 (555) 0142 738</div><div class="mail">MAIL@EXAMPLE.TLD</div>
  </div>
  <div class="member" style="left:520px">
    <div class="face" role="img" aria-label="Portrait of team member in yellow hard hat"></div>
    <h4>PETER LUND</h4><div class="role">Light protection maintainers</div>
    <div class="tel">+1 (555) 0142 738</div><div class="mail">MAIL@EXAMPLE.TLD</div>
  </div>

  <!-- work with band -->
  <section class="abs work" role="img" aria-label="Business handshake in dark suits">
    <h2>WORK WITH <span class="accent">HWN STRUCTURES</span></h2>
    <p>looking for reliable, high quality and cost effective building maintenance and/or property repair services in the city? hwn structures provide a wide range of maintenance and repair services to a variety of customers including domestic users, public sector entities and businesses across the city.</p>
    <div class="btn" style="left:350px;top:164px;width:100px;height:21px;font-size:7.5px">Make enquiry</div>
  </section>

  <!-- feedback -->
  <h2 class="sec-title" style="top:2390px">FEED<span class="accent">BACK</span></h2>
  <div class="abs say-box"><h3>What our students<br>have to say</h3></div>
  <div class="abs quote-card">
    <div class="avatar" role="img" aria-label="Portrait of reviewer"></div>
    <span class="qmark" style="left:48px;top:52px">“</span>
    <p>I work in project management and joined this course because I get great courses for less. The instructors are fantastic, interesting, and helpful. I plan to use this for a long time!</p>
    <span class="qmark" style="right:48px;top:92px">”</span>
    <span class="who">- Amira</span>
  </div>
  <div class="round" style="left:172px"><svg width="27" height="27" viewBox="0 0 27 27"><path d="M17 13.5H10m3-3l-3 3 3 3" fill="none" stroke="#fff" stroke-width="1.6"/></svg></div>
  <div class="round" style="left:212px"><svg width="27" height="27" viewBox="0 0 27 27"><path d="M10 13.5h7m-3-3l3 3-3 3" fill="none" stroke="#fff" stroke-width="1.6"/></svg></div>

  <!-- footer -->
  <footer class="abs footer">
    <svg class="abs" style="left:0;top:0" width="800" height="203" viewBox="0 0 800 203"><polygon points="0,52 400,0 800,52 800,203 0,203" fill="#000"/></svg>
    <div class="f-brand">HWN Structures</div>
    <p class="f-blurb">We plan, build and maintain homes and commercial sites, delivering careful workmanship and clear pricing from first visit to final handover.</p>
    <div class="col" style="left:279px"><h5>QUICK LINKS</h5><div class="links">home<br>service<br>projects<br>about us</div></div>
    <div class="col" style="left:397px"><h5>ADDRESS</h5>
      <div class="links" style="display:flex;gap:6px;align-items:center">
        <svg width="9" height="12" viewBox="0 0 9 12"><path d="M4.5 11.5S1 7 1 4.5a3.5 3.5 0 017 0C8 7 4.5 11.5 4.5 11.5z" fill="none" stroke="#fff"/><circle cx="4.5" cy="4.5" r="1.2" fill="#fff"/></svg>
        <span>12 Harbour Lane,<br>Leeds</span></div></div>
    <div class="col" style="left:524px"><h5>CONTACT US</h5>
      <div class="links" style="display:flex;gap:5px;align-items:center"><svg width="9" height="7" viewBox="0 0 10 7"><rect x=".5" y=".5" width="9" height="6" fill="none" stroke="#fff"/><path d="M.5 .5l4.5 3.5 4.5-3.5" fill="none" stroke="#fff"/></svg>hello@hwnstructures.example</div>
      <div class="links" style="display:flex;gap:5px;align-items:center;margin-top:3px"><svg width="8" height="8" viewBox="0 0 10 10"><path d="M2 1l2 2-1 1.5c.6 1.3 1.5 2.2 2.5 2.5L7 6l2 2-1.2 1.2C4.5 9 1 5.5.8 2.2z" fill="#fff"/></svg>555-0199</div></div>
    <div class="col" style="left:688px"><h5>FOLLOW US</h5><div><span class="dot"></span><span class="dot"></span><span class="dot"></span><span class="dot"></span></div></div>
    <div class="copy">copyright © hwn structures 2021 all rights reserved</div>
  </footer>

</main>
</body>
</html>
```